Business Card / Appointment Card for Physician

On one side it should give the logo, address, and contact information, and on the other side it should br an Appointment card.

One Side:
Logo (see attached files)
Board Certified American Orthopedic Surgery

1487 Harrowgate Ave.
Suite KM7
Bronx, NY 10527
Tel: (718) 552 - 1948
Fax: (718) 552 - 7210

628 Fourth Ave.
Suite 42
New York, NY 10087
Tel: (212) 734 - 2815

Second Side:
Appointment
give them a choice of Bronx or Mahattan office
For:
Date:
Time:

If you are unable to keep your appointment, please call (718) 263-5102 24hrs in advance.

Target Market(s)

People that need orthopedic surgery

Industry/Entity Type

Business

Contact Information for Business Card

smart and attractive

Requirements
Must have
• logo
• contact information on one side, appointment information on the other

```html
<!DOCTYPE html>
<html lang="en">
<head>
<meta charset="utf-8">
<title>Daniel R. Whitfield MD PC – Business &amp; Appointment Card</title>
<link rel="stylesheet" href="https://fonts.googleapis.com/css2?family=Raleway:wght@400;500;600&family=Montserrat:wght@600;700&display=swap">
<style>
  :root{
    --page:#ebe8e3;
    --card:#ffffff;
    --brand-blue:#1f5d99;
    --band-blue:#2d6699;
    --text-blue:#5b82ab;
    --label-blue:#2a9fe0;
    --accent-green:#5fa83f;
    --field:#f3f6ef;
    --box-blue:#2a9fe0;
  }
  *{box-sizing:border-box;margin:0;padding:0}
  html,body{width:1200px;height:675px;overflow:hidden;background:var(--page)}
  body{position:relative;font-family:"Raleway",sans-serif}

  .card{position:absolute;left:346px;width:508px;height:290px;background:var(--card);
        box-shadow:0 2px 6px rgba(0,0,0,.12)}
  .card--front{top:32px}
  .card--back{top:353px}

  .brand{position:absolute;left:0;right:0;text-align:center}
  .brand__mark{position:absolute;left:229px;top:26px;width:50px;height:50px;border-radius:50%;background:var(--brand-blue)}
  .brand__name{font-family:"Raleway",sans-serif;font-weight:500;font-size:21px;color:var(--brand-blue);letter-spacing:.2px;line-height:1}
  .brand__tagline{font-family:"Montserrat",sans-serif;font-weight:700;font-size:9.5px;color:var(--brand-blue);margin-top:4px;letter-spacing:.1px}
  .card--front .brand{top:90px}
  .card--back .brand{top:28px}

  .band{position:absolute;left:0;right:0;height:28px;background:var(--band-blue);color:#fff;
        display:flex;align-items:center;justify-content:center}
  .band--credential{top:146px;font-family:"Raleway",sans-serif;font-weight:600;font-size:12.5px;letter-spacing:1.2px}
  .band--title{top:72px;font-family:"Montserrat",sans-serif;font-weight:700;font-size:15px;letter-spacing:1.3px}

  .office{position:absolute;top:183px;font-size:13px;line-height:15px;color:var(--text-blue)}
  .office--bronx{left:66px}
  .office--manhattan{left:299px}
  .office__line{display:flex;align-items:center;height:15px}
  .office__line--indent{padding-left:15px}
  .icon{width:11px;height:11px;margin-right:4px;flex:none}

  .choice{position:absolute;top:112px;display:flex;align-items:center;
          font-family:"Montserrat",sans-serif;font-weight:700;font-size:13px;color:var(--accent-green)}
  .choice--bronx{left:94px}
  .choice--manhattan{left:290px}
  .choice__box{width:22px;height:22px;border:2px solid var(--box-blue);margin-right:10px;background:#fff}

  .field-label{position:absolute;font-family:"Montserrat",sans-serif;font-weight:700;font-size:16px;
               color:var(--label-blue);letter-spacing:.8px}
  .field{position:absolute;background:var(--field)}
  .label--for{left:36px;top:152px}
  .field--for{left:95px;top:142px;width:378px;height:40px}
  .label--date{left:36px;top:206px}
  .field--date{left:95px;top:196px;width:193px;height:40px}
  .label--time{left:297px;top:206px}
  .field--time{left:355px;top:196px;width:118px;height:40px}

  .notice{position:absolute;left:0;right:0;top:250px;text-align:center;
          font-family:"Montserrat",sans-serif;font-weight:600;font-size:8.4px;color:var(--band-blue);letter-spacing:.3px}
</style>
</head>
<body>

<section class="card card--front" aria-label="Business card">
  <div class="brand__mark" aria-hidden="true"></div>
  <div class="brand">
    <p class="brand__name">DANIEL R. WHITFIELD MD PC</p>
    <p class="brand__tagline">ORTHOPAEDIC SURGERY &amp; SPORTS MEDICINE</p>
  </div>

  <div class="band band--credential">BOARD CERTIFIED AMERICAN ORTHOPEDIC SURGERY</div>

  <address class="office office--bronx" style="font-style:normal">
    <div class="office__line">
      <svg class="icon" viewBox="0 0 12 12"><path d="M6 0.5a4 4 0 0 0-4 4c0 3 4 7 4 7s4-4 4-7a4 4 0 0 0-4-4z" fill="var(--accent-green)"/><circle cx="6" cy="4.5" r="1.5" fill="#fff"/></svg>
      1487 Harrowgate Ave.
    </div>
    <div class="office__line office__line--indent">Suite KM7</div>
    <div class="office__line office__line--indent">Bronx, NY 10527</div>
    <div class="office__line">
      <svg class="icon" viewBox="0 0 12 12"><circle cx="6" cy="6" r="6" fill="var(--accent-green)"/><path d="M4 3l1.2 1.5-.6.9c.4.8 1 1.4 1.8 1.8l.9-.6L8.8 7.8 8 9C5.5 8.7 3.3 6.5 3 4z" fill="#fff"/></svg>
      Tel (718) 552 - 1948
    </div>
    <div class="office__line">
      <svg class="icon" viewBox="0 0 12 12"><circle cx="6" cy="6" r="6" fill="var(--accent-green)"/><rect x="3" y="5" width="6" height="3" fill="#fff"/><rect x="4" y="3" width="4" height="2" fill="#fff"/><rect x="4" y="8" width="4" height="1.3" fill="#fff"/></svg>
      Fax (718) 552 - 7210
    </div>
  </address>

  <address class="office office--manhattan" style="font-style:normal">
    <div class="office__line">
      <svg class="icon" viewBox="0 0 12 12"><path d="M6 0.5a4 4 0 0 0-4 4c0 3 4 7 4 7s4-4 4-7a4 4 0 0 0-4-4z" fill="var(--accent-green)"/><circle cx="6" cy="4.5" r="1.5" fill="#fff"/></svg>
      628 Fourth Ave.
    </div>
    <div class="office__line office__line--indent">Suite 42</div>
    <div class="office__line office__line--indent">New York, NY 10087</div>
    <div class="office__line">
      <svg class="icon" viewBox="0 0 12 12"><circle cx="6" cy="6" r="6" fill="var(--accent-green)"/><path d="M4 3l1.2 1.5-.6.9c.4.8 1 1.4 1.8 1.8l.9-.6L8.8 7.8 8 9C5.5 8.7 3.3 6.5 3 4z" fill="#fff"/></svg>
      Tel (212) 734 - 2815
    </div>
  </address>
</section>

<section class="card card--back" aria-label="Appointment card">
  <div class="brand">
    <p class="brand__name">DANIEL R. WHITFIELD MD PC</p>
    <p class="brand__tagline">ORTHOPAEDIC SURGERY &amp; SPORTS MEDICINE</p>
  </div>

  <div class="band band--title">APPOINTMENT CARD</div>

  <div class="choice choice--bronx"><span class="choice__box"></span>Bronx, NY 10527</div>
  <div class="choice choice--manhattan"><span class="choice__box"></span>New York, NY 10087</div>

  <span class="field-label label--for">FOR</span>
  <div class="field field--for"></div>
  <span class="field-label label--date">DATE</span>
  <div class="field field--date"></div>
  <span class="field-label label--time">TIME</span>
  <div class="field field--time"></div>

  <p class="notice">If you are unable to keep your appointment, please call (718) 263-5102 24hrs in advance.</p>
</section>

</body>
</html>
```